Veltrona Services

Double sided business cards with color on front and black and white on back. I have basic ideas and graphics, but am looking for someone to take them to the next level

```html
<!DOCTYPE html>
<html lang="en">
<head>
<meta charset="utf-8">
<title>Veltrona Services – Business Card</title>
<link href="https://fonts.googleapis.com/css2?family=Noto+Sans:wght@600;700&display=swap" rel="stylesheet">
<style>
  :root {
    --paper: #ffffff;
    --card: #000000;
    --ink: #ffffff;
    --shade: #161616;
    --shade-ink: #262626;
  }
  html, body {
    margin: 0;
    padding: 0;
    width: 1200px;
    height: 756px;
    overflow: hidden;
    background: var(--paper);
  }
  .canvas {
    position: relative;
    width: 1200px;
    height: 756px;
    background: var(--paper);
  }
  .card {
    position: absolute;
    left: 37px;
    top: 32px;
    width: 1126px;
    height: 686px;
    background: var(--card);
    overflow: hidden;
  }
  .backdrop-mark {
    position: absolute;
    left: -230px;
    top: 40px;
    width: 560px;
    height: 560px;
    border-radius: 50%;
    background: var(--shade);
  }
  .backdrop-mark__name {
    position: absolute;
    left: 20px;
    top: 292px;
    margin: 0;
    font-family: "Noto Sans", sans-serif;
    font-weight: 600;
    font-size: 46px;
    letter-spacing: 2px;
    color: var(--shade-ink);
  }
  .brand-mark {
    position: absolute;
    left: 403px;
    top: 134px;
    width: 226px;
    height: 226px;
    border: 36px solid var(--ink);
    border-radius: 50%;
    display: flex;
    align-items: center;
    justify-content: center;
  }
  .brand-mark__name {
    font-family: "Noto Sans", sans-serif;
    font-weight: 600;
    font-size: 30px;
    letter-spacing: 1px;
    color: var(--ink);
  }
  .company-name {
    position: absolute;
    left: 0;
    width: 1126px;
    top: 456px;
    margin: 0;
    text-align: center;
    font-family: "Noto Sans", sans-serif;
    font-weight: 600;
    font-size: 49px;
    line-height: 60px;
    letter-spacing: 3px;
    color: var(--ink);
  }
  .company-phone {
    position: absolute;
    left: 0;
    width: 1126px;
    top: 515px;
    margin: 0;
    text-align: center;
    font-family: "Noto Sans", sans-serif;
    font-weight: 700;
    font-size: 35px;
    line-height: 44px;
    letter-spacing: 3px;
    color: var(--ink);
  }
</style>
</head>
<body>
  <main class="canvas">
    <section class="card">
      <div class="backdrop-mark" aria-hidden="true"></div>
      <p class="backdrop-mark__name" aria-hidden="true">VELTRONA</p>
      <div class="brand-mark">
        <span class="brand-mark__name">VELTRONA</span>
      </div>
      <h1 class="company-name">VELTRONA SERVICES</h1>
      <p class="company-phone">555-014-7823</p>
    </section>
  </main>
</body>
</html>
```